Help! We need PROFESSIONAL E-mail Signatures that POP!

9/12 UPDATE:
We have extended the deadline.
Also the logo we want used for Melsford has changed.

We have 8 employees working for three companies. We want our e-mail signatures to be the same format and cohesive, but each person has one company of the three that needs to be highlighted.
- Logos are attached and spreadsheet shows what information is needed for each employee as well as which of the logos should be the primary logo - first one displayed and slightly larger than the others.
- Please create one design first using the information for Daniel Wystan from Line 2 of the spreadsheet (provided three versions - Numbers, Excel, PDF
- All components need to be able to be changed or deleted.
- We need to be able to easily create new signatures for new employees
Updates

Need extra days to review

If you submitted a design prior to yesterday afternoon, please see original brief for the updated Melsford logo. This is the version of the Melsford logo that will be used for all the email signatures. The spreadsheet with the info for all 8 employees show different versions of this logo for different employees. Ignore that. Use this one logo in the design along with the Pelna and Brisk logos as indicated on the spreadsheet. Thanks!

Target Market(s)

New/existing clients!

Industry/Entity Type

Property development, commercial construction, property management

Font styles to use
Sans Serif

Requirements
Must have
• A lot of info with a clean look
Nice to have
• Consistency and cohesion
Should not have
• Too many elements - UPDATE: No photos - thanks!

```html
<!DOCTYPE html>
<html lang="en">
<head>
<meta charset="utf-8">
<title>Email Signatures – Daniel Wystan</title>
<link href="https://fonts.googleapis.com/css2?family=Roboto+Slab:wght@700&family=Roboto:wght@300;400;700&display=swap" rel="stylesheet">
<style>
  :root {
    --orange: #f15a24;
    --blue: #1a75bb;
    --green: #7dc242;
    --ink: #1e1e1e;
    --charcoal: #3d3d3d;
    --band: #c9c9c9;
    --page: #ffffff;
  }
  html, body { margin: 0; padding: 0; }
  body {
    width: 1200px; height: 1136px; overflow: hidden;
    background: var(--page);
    font-family: "Roboto", Arial, sans-serif;
    color: var(--ink);
    position: relative;
  }
  .signature {
    position: absolute; left: 15px; width: 1150px; height: 329px;
    background: #fff;
    box-shadow: 9px 9px 6px rgba(0,0,0,.6);
  }
  .signature--pelna { top: 15px; --accent: var(--orange); --accent-soft: #f7a882; }
  .signature--brisk { top: 393px; --accent: var(--blue); --accent-soft: #9fc0e3; }
  .signature--melsford { top: 772px; --accent: var(--green); --accent-soft: #b9de98; }

  .person-name {
    position: absolute; left: 34px; top: 18px; margin: 0;
    font-family: "Roboto Slab", Georgia, serif; font-weight: 700;
    font-size: 40px; line-height: 1; color: var(--ink);
  }
  .person-name .first { color: var(--accent); }
  .person-role {
    position: absolute; left: 34px; top: 79px; margin: 0;
    font-size: 17px; font-weight: 400;
  }
  .divider { position: absolute; left: 34px; top: 108px; height: 5px; width: 215px; }
  .divider .rule { position: absolute; left: 0; top: 0; width: 137px; height: 5px; background: var(--charcoal); border-radius: 3px; }
  .divider .dash { position: absolute; top: 0; width: 16px; height: 5px; background: var(--accent); border-radius: 3px; }
  .divider .dash-1 { left: 147px; }
  .divider .dash-2 { left: 168px; }

  .contact { position: absolute; }
  .contact .label { display: block; font-size: 10.5px; color: var(--ink); margin-left: 2px; }
  .contact .value { display: flex; align-items: center; gap: 8px; font-size: 16px; font-weight: 700; margin-top: 3px; white-space: nowrap; }
  .icon { width: 12px; height: 12px; border-radius: 50%; flex: none; box-sizing: border-box; }
  .icon--solid { background: var(--accent); }
  .icon--ring { border: 2px solid var(--accent); }
  .c-direct { left: 34px; top: 124px; }
  .c-office { left: 34px; top: 164px; }
  .c-address { left: 264px; top: 124px; }
  .c-email { left: 264px; top: 164px; }
  .c-web { left: 486px; top: 164px; }

  .license { position: absolute; left: 34px; top: 203px; margin: 0; font-size: 16.5px; font-weight: 300; color: #333; }

  .brand-art { position: absolute; left: 680px; top: 60px; width: 470px; height: 173px; }
  .brand { position: absolute; display: flex; align-items: center; gap: 7px; font-weight: 700; white-space: nowrap; }
  .brand .mark { display: inline-block; }
  .brand--primary { font-size: 34px; }
  .brand--primary .mark { width: 26px; height: 26px; }
  .brand--minor { font-size: 22px; }
  .brand--minor .mark { width: 16px; height: 16px; }
  .brand--melsford { color: var(--green); }
  .brand--melsford .mark { background: var(--green); }
  .brand--pelna { color: var(--charcoal); }
  .brand--pelna .mark { background: var(--charcoal); border-radius: 50%; }
  .brand--brisk { color: var(--blue); }
  .brand--brisk .mark { background: var(--blue); }

  .notice {
    position: absolute; left: 0; top: 233px; width: 1150px; height: 96px;
    box-sizing: border-box; padding: 8px 12px 0 14px; margin: 0;
    background: var(--band);
    font-size: 13.3px; line-height: 19px; font-weight: 300; color: #333;
  }
</style>
</head>
<body>

<!-- Pelna highlighted -->
<section class="signature signature--pelna">
  <h1 class="person-name"><span class="first">Daniel</span> Wystan</h1>
  <p class="person-role">CEO/Owner</p>
  <div class="divider"><span class="rule"></span><span class="dash dash-1"></span><span class="dash dash-2"></span></div>
  <div class="contact c-direct"><span class="label">Direct phone number</span><span class="value"><i class="icon icon--solid"></i>555-214-3390</span></div>
  <div class="contact c-office"><span class="label">Melsford</span><span class="value"><i class="icon icon--solid"></i>555-672-1048 x210</span></div>
  <div class="contact c-address"><span class="label">Address</span><span class="value"><i class="icon icon--ring"></i>48 N. Cedar Ave., Ste 3B, Larkfield IL 60599</span></div>
  <div class="contact c-email"><span class="label">Email</span><span class="value"><i class="icon icon--ring"></i>dwystan@melsford.com</span></div>
  <div class="contact c-web"><span class="label">Web</span><span class="value"><i class="icon icon--ring"></i>www.melsford.com</span></div>
  <p class="license">IL RE Lic#: 400.551208 Chicago GC Lic #: TGC051193</p>
  <div class="brand-art">
    <svg width="470" height="173" viewBox="0 0 470 173" aria-hidden="true" style="position:absolute;left:0;top:0">
      <polygon points="224,169 256,112 306,169" fill="var(--accent-soft)"/>
      <polygon points="232,169 258,101 286,169" fill="var(--accent)"/>
      <rect x="20" y="167" width="450" height="4" fill="var(--accent)"/>
    </svg>
    <span class="brand brand--minor brand--melsford" style="left:40px;top:94px"><i class="mark"></i>Melsford</span>
    <span class="brand brand--primary brand--pelna" style="left:204px;top:46px"><i class="mark"></i>Pelna</span>
    <span class="brand brand--minor brand--brisk" style="left:372px;top:94px"><i class="mark"></i>Brisk</span>
  </div>
  <p class="notice">CONFIDENTIALITY NOTICE: This e-mail is intended only for the recipient named and may contain confidential, privileged, and exempt from disclosure under applicable laws. If you are not the named recipient, you may have received this transmission in error. We ask that you, please immediately notify us by e-mail at operations@melsford.com and remove this and all attached file(s) from your system. You are notified that any disclosure, copying, distribution, or use of the information in this transmission if you are not the intended recipient is prohibited and may expose you to liability.</p>
</section>

<!-- Brisk highlighted -->
<section class="signature signature--brisk">
  <h1 class="person-name"><span class="first">Daniel</span> Wystan</h1>
  <p class="person-role">CEO/Owner</p>
  <div class="divider"><span class="rule"></span><span class="dash dash-1"></span><span class="dash dash-2"></span></div>
  <div class="contact c-direct"><span class="label">Direct phone number</span><span class="value"><i class="icon icon--solid"></i>555-214-3390</span></div>
  <div class="contact c-office"><span class="label">Melsford</span><span class="value"><i class="icon icon--solid"></i>555-672-1048 x210</span></div>
  <div class="contact c-address"><span class="label">Address</span><span class="value"><i class="icon icon--ring"></i>48 N. Cedar Ave., Ste 3B, Larkfield IL 60599</span></div>
  <div class="contact c-email"><span class="label">Email</span><span class="value"><i class="icon icon--ring"></i>dwystan@melsford.com</span></div>
  <div class="contact c-web"><span class="label">Web</span><span class="value"><i class="icon icon--ring"></i>www.melsford.com</span></div>
  <p class="license">IL RE Lic#: 400.551208 Chicago GC Lic #: TGC051193</p>
  <div class="brand-art">
    <svg width="470" height="173" viewBox="0 0 470 173" aria-hidden="true" style="position:absolute;left:0;top:0">
      <polygon points="200,169 245,104 296,169" fill="var(--accent-soft)"/>
      <polygon points="216,169 248,93 280,169" fill="var(--accent)"/>
      <rect x="20" y="167" width="450" height="4" fill="var(--accent)"/>
    </svg>
    <span class="brand brand--minor brand--melsford" style="left:40px;top:82px"><i class="mark"></i>Melsford</span>
    <span class="brand brand--primary brand--brisk" style="left:196px;top:12px"><i class="mark"></i>Brisk</span>
    <span class="brand brand--minor brand--pelna" style="left:340px;top:86px"><i class="mark"></i>Pelna</span>
  </div>
  <p class="notice">CONFIDENTIALITY NOTICE: This e-mail is intended only for the recipient named and may contain confidential, privileged, and exempt from disclosure under applicable laws. If you are not the named recipient, you may have received this transmission in error. We ask that you, please immediately notify us by e-mail at operations@melsford.com and remove this and all attached file(s) from your system. You are notified that any disclosure, copying, distribution, or use of the information in this transmission if you are not the intended recipient is prohibited and may expose you to liability.</p>
</section>

<!-- Melsford highlighted -->
<section class="signature signature--melsford">
  <h1 class="person-name"><span class="first">Daniel</span> Wystan</h1>
  <p class="person-role">CEO/Owner</p>
  <div class="divider"><span class="rule"></span><span class="dash dash-1"></span><span class="dash dash-2"></span></div>
  <div class="contact c-direct"><span class="label">Direct phone number</span><span class="value"><i class="icon icon--solid"></i>555-214-3390</span></div>
  <div class="contact c-office"><span class="label">Melsford</span><span class="value"><i class="icon icon--solid"></i>555-672-1048 x210</span></div>
  <div class="contact c-address"><span class="label">Address</span><span class="value"><i class="icon icon--ring"></i>48 N. Cedar Ave., Ste 3B, Larkfield IL 60599</span></div>
  <div class="contact c-email"><span class="label">Email</span><span class="value"><i class="icon icon--ring"></i>dwystan@melsford.com</span></div>
  <div class="contact c-web"><span class="label">Web</span><span class="value"><i class="icon icon--ring"></i>www.melsford.com</span></div>
  <p class="license">IL RE Lic#: 400.551208 Chicago GC Lic #: TGC051193</p>
  <div class="brand-art">
    <svg width="470" height="173" viewBox="0 0 470 173" aria-hidden="true" style="position:absolute;left:0;top:0">
      <polygon points="214,169 256,114 298,169" fill="var(--accent-soft)"/>
      <polygon points="228,169 258,103 288,169" fill="var(--accent)"/>
      <rect x="20" y="167" width="450" height="4" fill="var(--accent)"/>
    </svg>
    <span class="brand brand--primary brand--melsford" style="left:186px;top:6px"><i class="mark"></i>Melsford</span>
    <span class="brand brand--minor brand--pelna" style="left:72px;top:100px"><i class="mark"></i>Pelna</span>
    <span class="brand brand--minor brand--brisk" style="left:376px;top:100px"><i class="mark"></i>Brisk</span>
  </div>
  <p class="notice">CONFIDENTIALITY NOTICE: This e-mail is intended only for the recipient named and may contain confidential, privileged, and exempt from disclosure under applicable laws. If you are not the named recipient, you may have received this transmission in error. We ask that you, please immediately notify us by e-mail at operations@melsford.com and remove this and all attached file(s) from your system. You are notified that any disclosure, copying, distribution, or use of the information in this transmission if you are not the intended recipient is prohibited and may expose you to liability.</p>
</section>

</body>
</html>
```